High end boutique food product label

We are looking for a label design to be used on our range of high end food products. We don't have a design or colour scheme in mind and are interested to see what ideas are submitted.
We would like it to feel sophisticated, chic, and eye-catching.
All of our products are handmade in Australia using Australian ingredients.
The graphics for the label will need to be scaleable to be fit a variety of labels from small squat jars with labels sized 3.5cm high and 7cm wide, to tall thin bottles with labels that are 14cm high and 4.5cm wide.
We would be interested in working with the winning designer to create these different sized labels.
The label submitted for this project should be 14cm high and 4.5cm wide, it should include our logo (file supplied in .jpeg and .ai), the product name 'Extra Virgin Olive Oil' and the size '250ml'.
This is just the front label on a bottle, we are not expecting a rear label to be created currently.
You are welcome to use any fonts you think will look good but the fonts used in our logo are Allaina Medium and Bebas Kai Regular.

```html
<!DOCTYPE html>
<html lang="en">
<head>
<meta charset="utf-8">
<title>Extra Virgin Olive Oil – Front Label</title>
<link rel="stylesheet" href="https://fonts.googleapis.com/css2?family=Playfair+Display:wght@400&display=swap">
<style>
  :root {
    --backdrop: #2a0f20;
    --label-green: #a5a83b;
    --label-cream: #f4ecd2;
    --olive-indigo: #4a1f7a;
    --olive-plum: #6a1c3e;
    --olive-magenta: #7d1d62;
    --olive-beige: #d9c7a4;
  }
  html, body {
    margin: 0;
    padding: 0;
    width: 1200px;
    height: 1200px;
    overflow: hidden;
    background: var(--backdrop);
  }
  .canvas {
    position: relative;
    width: 1200px;
    height: 1200px;
  }
  .label {
    position: absolute;
    left: 440px;
    top: 80px;
    width: 321px;
    height: 1040px;
    background: var(--label-green);
    font-family: "Playfair Display", Georgia, serif;
    font-weight: 400;
    font-variant-numeric: lining-nums;
    color: var(--label-cream);
    text-align: center;
    overflow: hidden;
  }
  .label__artwork {
    position: absolute;
    left: 0;
    top: 0;
    width: 321px;
    height: 711px;
    display: block;
  }
  .label__text {
    position: absolute;
    left: 0;
    width: 100%;
    margin: 0;
    font-weight: 400;
    line-height: 1;
    white-space: nowrap;
  }
  .label__brand {
    top: 76px;
    font-size: 16px;
  }
  .label__brand-mark {
    display: inline-block;
    width: 6px;
    height: 6px;
    border-radius: 50%;
    background: var(--label-cream);
    vertical-align: middle;
    margin-right: 6px;
    position: relative;
    top: -1px;
  }
  .label__grade {
    top: 803px;
    font-size: 21px;
  }
  .label__product {
    top: 836px;
    font-size: 37px;
    letter-spacing: 3px;
  }
  .label__origin {
    top: 905px;
    font-size: 15px;
  }
  .label__volume {
    top: 992px;
    font-size: 17px;
  }
</style>
</head>
<body>
  <main class="canvas">
    <section class="label">
      <svg class="label__artwork" viewBox="0 0 321 711" role="img" aria-label="Abstract illustration of overlapping dark olives in indigo, plum and magenta with green leaves on a beige ground">
        <defs>
          <linearGradient id="artwork-tones" x1="0" y1="0" x2="1" y2="1">
            <stop offset="0" stop-color="#4a1f7a"/>
            <stop offset="0.45" stop-color="#6a1c3e"/>
            <stop offset="0.75" stop-color="#4a1f7a"/>
            <stop offset="1" stop-color="#d9c7a4"/>
          </linearGradient>
        </defs>
        <rect width="321" height="711" fill="url(#artwork-tones)"/>
      </svg>
      <div class="label__text label__brand"><span class="label__brand-mark"></span>Bellgrove Pantry</div>
      <div class="label__text label__grade">Extra Virgin</div>
      <h1 class="label__text label__product">OLIVE OIL</h1>
      <div class="label__text label__origin">100% Australian made</div>
      <div class="label__text label__volume">250ml</div>
    </section>
  </main>
</body>
</html>
```